Velmora Care Collective Presentation Folder, for Cancer Awareness, VERY COLORFUL AND MODERN

Presentation Folder I know pretty much what i want so it should be very eazy , I have included files from folders I use now rebrand them to my new company they will be fine, no sense re creating the wheel
Full Bleed Size
20.87" x 16.68"
53 x 42.4 cm
6260 x 5004 pixels
Document Trim Size
20.75" x 16.56"
52.7 x 42.1 cm
6225 x 4969 pixels

Industry/Entity Type

Medical

Font styles to use
Serif

Colors

Designer to choose colors to be used in the design.

Requirements
Must have
• really I am not looking for some one to redesign, we like our folder front page and would like to see new word information added., there are two folder front pages to choose from
• So Keep the original front page and redesign the back page and the pockets
• Can Make your Design off of one of the ones I already uploaded
Nice to have
• Keep the same color schemes, Keep the original front page and redesign the back page and the pockets
Should not have
• DO not recreate the front covers, use what I gave you and just rebrand

```html
<!DOCTYPE html>
<html lang="en">
<head>
<meta charset="utf-8">
<title>Velmora Care Collective – Hereditary Cancer Screening Folder</title>
<link href="https://fonts.googleapis.com/css2?family=Raleway:wght@300;400;500;700&display=swap" rel="stylesheet">
<style>
  :root {
    --stage: #3a3a3a;
    --paper: #ffffff;
    --ink: #2e3350;
    --pink: #e8718a;
    --pink-soft: #f4a9b9;
    --rose: #d4558a;
    --magenta: #9a2f8e;
    --sky: #4fbde9;
    --band-grey: #6f6e72;
    --band-grey-light: #8a898d;
    --title-pink: #ea7a9c;
  }
  * { box-sizing: border-box; margin: 0; padding: 0; }
  html, body { width: 1200px; height: 902px; overflow: hidden; }
  body {
    background: var(--stage);
    font-family: "Raleway", sans-serif;
    color: var(--ink);
    position: relative;
  }
  .panel {
    position: absolute;
    top: 104px;
    width: 528px;
    height: 667px;
    background: var(--paper);
    overflow: hidden;
  }
  .panel--inside { left: 41px; }
  .panel--back { left: 627px; }

  /* inside panel */
  .ribbon-accent {
    position: absolute;
    right: 0; top: 0;
    width: 66px; height: 440px;
    background: linear-gradient(180deg, var(--magenta) 0%, #e7b3cf 45%, var(--sky) 75%, rgba(79,189,233,0.2) 100%);
    border-radius: 50px 0 0 0;
    z-index: 2;
  }
  .intro {
    position: absolute;
    left: 24px; top: 39px;
    width: 430px;
    font-size: 11px;
    line-height: 14.5px;
    text-align: justify;
    color: var(--ink);
  }
  .intro p + p { margin-top: 14px; }
  .callout {
    position: absolute;
    left: 0; top: 234px;
    width: 470px; height: 77px;
    background: linear-gradient(90deg, var(--pink) 0%, var(--pink-soft) 70%, rgba(244,169,185,0.6) 100%);
    color: #fff;
    font-weight: 700;
    font-size: 16.5px;
    line-height: 21px;
    padding: 13px 20px 0 27px;
  }
  .family-photo {
    position: absolute;
    left: 0; top: 311px;
    width: 100%; height: 356px;
    background: linear-gradient(180deg, #6cc4ee 0%, #bfe6f6 50%, #efe6d6 70%, #e8dcc6 100%);
  }

  /* back panel */
  .title {
    position: absolute;
    left: 0; top: 101px;
    width: 100%;
    text-align: center;
    font-weight: 300;
    font-size: 28px;
    letter-spacing: 0.5px;
    color: var(--title-pink);
  }
  .gatekeeper {
    position: absolute;
    left: 46px; top: 139px;
    width: 427px; height: 32px;
    background: var(--band-grey-light);
    color: #fff;
    font-size: 14.5px;
    line-height: 32px;
    text-align: center;
  }
  .obligation {
    position: absolute;
    left: 0; top: 181px;
    width: 100%;
    text-align: center;
    font-size: 11px;
    line-height: 15px;
    color: var(--ink);
  }
  .ribbon-tile {
    position: absolute;
    border-radius: 40px 40px 6px 6px;
    background: linear-gradient(180deg, #e47aa6, var(--rose));
    color: #fff;
    font-size: 6.5px;
    line-height: 7.5px;
    text-transform: uppercase;
    display: flex;
    align-items: center;
    justify-content: center;
    gap: 2px;
    text-align: center;
  }
  .ribbon-tile span { transform: rotate(60deg); display: block; width: 38px; }
  .ribbon-tile--feature {
    background: linear-gradient(90deg, var(--sky) 0%, var(--sky) 40%, #d79ac4 60%, var(--magenta) 100%);
    font-size: 10px;
    line-height: 11px;
    gap: 8px;
  }
  .ribbon-tile--feature span { width: 62px; }
  .footer-band {
    position: absolute;
    left: 0; top: 570px;
    width: 100%; height: 52px;
    background: var(--band-grey);
    display: flex;
    align-items: center;
    padding-left: 30px;
    gap: 14px;
    color: #fff;
  }
  .brand-mark {
    width: 42px; height: 42px;
    border-radius: 50%;
    background: #fff;
    flex: none;
  }
  .brand-name { font-size: 11px; font-weight: 500; color: #fff; width: 60px; line-height: 13px; }
  .tagline { font-size: 20px; font-weight: 400; margin-left: 10px; }
</style>
</head>
<body>
  <section class="panel panel--inside">
    <div class="ribbon-accent" role="img" aria-label="Pink, purple and blue awareness ribbon decoration"></div>
    <div class="intro">
      <p>There are many benefits to getting tested, regardless of the eventual result. If one of your family members — however distant — had cancer, there is a chance that you inherited a gene mutation that not only increases your personal risk of cancer, but also could be passed to the next generation. Those who are carriers of hereditary cancer gene mutations, could be at risk of getting cancer earlier in life than the general population. The sooner genetic testing is done, the more likely it is that the risk can be managed appropriately.</p>
      <p>Hereditary cancer screening provides vital information to help people with a strong personal or family history of cancer understand their own risk of developing the disease. With this information, they can take steps to Potentially Prevent Cancer, Delay the Onset of Cancer or Catch it at an Earlier stage when outcomes and survival rates are Better.</p>
    </div>
    <div class="callout">Identifying an inherited genetic mutation has the potential to prevent cancer and save lives.</div>
    <div class="family-photo" role="img" aria-label="Photo of a multi-generation family in white clothing walking hand in hand on a sunny beach"></div>
  </section>

  <section class="panel panel--back">
    <h1 class="title">HEREDITARY CANCER SCREENING</h1>
    <div class="gatekeeper">DOCTORS ARE THE GATEKEEPERS TO GENETIC TESTING.</div>
    <p class="obligation">WE HAVE AN OBLIGATION TO HELP PATIENTS UNDERSTAND GENETIC<br>RISK AND HOW TESTING CAN GUIDE HEATH CARE DECISIONS.</p>

    <div class="ribbon-tile" style="left:28px;top:372px;width:93px;height:125px" role="img" aria-label="Pink ribbon for breast and ovarian cancer"><span>Breast Cancer</span><span>Ovarian Cancer</span></div>
    <div class="ribbon-tile" style="left:127px;top:393px;width:69px;height:98px" role="img" aria-label="Pink ribbon for endometrial and gastric cancer"><span>Endometrial Cancer</span><span>Gastric Cancer</span></div>
    <div class="ribbon-tile ribbon-tile--feature" style="left:193px;top:282px;width:136px;height:188px" role="img" aria-label="Blue and purple ribbon for pancreatic and colorectal cancer"><span>Pancreatic Cancer</span><span>Colorectal Cancer</span></div>
    <div class="ribbon-tile" style="left:319px;top:391px;width:71px;height:92px" role="img" aria-label="Pink ribbon for melanoma and lung cancer"><span>Melanoma Cancer</span><span>Lung Cancer</span></div>
    <div class="ribbon-tile" style="left:395px;top:364px;width:93px;height:122px" role="img" aria-label="Pink ribbon for prostate and colon cancer"><span>Prostate Cancer</span><span>Colon Cancer</span></div>

    <div class="footer-band">
      <div class="brand-mark"></div>
      <div class="brand-name">Velmora Care Collective</div>
      <div class="tagline">The test you order FOR your patients</div>
    </div>
  </section>
</body>
</html>
```